Executive Coaching and Spiritual Development Company needs a business card design.

We need a business card design for our company. We already have a logo that was created through Loomquarry that we will submit and would like to see this work on black, blue and white backgrounds. Our personal information should be included as well. The design should communicate trust, spirituality, support and partnership.

Industry/Entity Type

Business

Colors
0255a3
33a6d7
ffffff
000000
474747

Requirements
Nice to have
• The colors offered here are just ideas--we are open to other suggestions, too.

```html
<!DOCTYPE html>
<html lang="en">
<head>
<meta charset="utf-8">
<title>Stillharbor Business Card</title>
<link rel="stylesheet" href="https://fonts.googleapis.com/css2?family=Lato:wght@400;700;900&display=swap">
<style>
  :root {
    --backdrop: #2b2b2b;
    --brand-blue: #0255a3;
    --card-blue: #0a5cb4;
    --ink-navy: #0e2238;
    --ink-dark: #1a1a1a;
    --paper: #f4f4f4;
    --circle-ring: #1d1d1d;
  }
  * { box-sizing: border-box; margin: 0; padding: 0; }
  html, body {
    width: 1200px; height: 900px; overflow: hidden;
    background: var(--backdrop);
    font-family: "Lato", sans-serif;
  }
  .canvas { position: relative; width: 1200px; height: 900px; }
  .card {
    position: absolute; width: 560px; height: 320px;
    box-shadow: 0 14px 30px rgba(0,0,0,.5);
    overflow: hidden;
  }
  .card-back { left: 80px; top: 90px; background: var(--card-blue); }
  .card-front { left: 560px; top: 490px; background: var(--paper); }

  .brand { display: flex; align-items: center; gap: 16px; }
  .brand-mark {
    width: 70px; height: 70px; border-radius: 50%;
    border: 3px solid var(--circle-ring);
  }
  .brand-name { font-weight: 700; font-size: 50px; letter-spacing: .5px; }

  .card-back .brand {
    position: absolute; left: 95px; top: 105px;
  }
  .card-back .brand-name { color: var(--ink-navy); }
  .card-back .brand-mark { border-color: var(--ink-navy); }
  .tagline {
    position: absolute; left: 0; right: 0; top: 230px; text-align: center;
    font-size: 12px; letter-spacing: 3px; color: var(--ink-navy);
  }

  .bands { position: absolute; inset: 0; }
  .card-front .brand { position: absolute; left: 40px; top: 60px; }
  .card-front .brand-name { color: var(--ink-dark); }

  .contact {
    position: absolute; right: 30px; top: 82px; text-align: right;
    color: var(--ink-dark); font-size: 15px; line-height: 1.55;
  }
  .contact .address { color: var(--brand-blue); font-weight: 700; margin-bottom: 8px; line-height: 1.25; }
  .contact .line { display: flex; justify-content: flex-end; align-items: center; gap: 8px; }
  .contact svg { width: 16px; height: 14px; }
  .contact .web { color: var(--brand-blue); font-weight: 900; font-size: 20px; margin-top: 6px; }

  .person { position: absolute; left: 40px; top: 210px; }
  .person-name { color: var(--brand-blue); font-weight: 900; font-size: 20px; letter-spacing: .3px; }
  .person-role { color: var(--ink-dark); font-weight: 700; font-size: 15px; }
</style>
</head>
<body>
<main class="canvas">
  <section class="card card-back">
    <div class="brand">
      <span class="brand-mark"></span>
      <span class="brand-name">Stillharbor</span>
    </div>
    <p class="tagline">YOUR SLOGAN / TAGLINE HERE</p>
  </section>

  <section class="card card-front">
    <svg class="bands" viewBox="0 0 560 320" preserveAspectRatio="none">
      <path d="M0 0 H560 V34 H470 Q455 34 445 18 Q438 10 425 10 H0 Z" fill="var(--brand-blue)"/>
      <path d="M0 312 H150 Q165 312 172 300 Q180 288 195 288 H560 V320 H0 Z" fill="var(--brand-blue)"/>
    </svg>

    <div class="brand">
      <span class="brand-mark"></span>
      <span class="brand-name">Stillharbor</span>
    </div>

    <div class="contact">
      <div class="address">Halverton, Queensland,<br>Australia 4100</div>
      <div class="line">555-214-7730
        <svg viewBox="0 0 16 14"><path d="M2 5 Q8 0 14 5 L12 7 L10 5 H6 L4 7 Z M4 8 H12 V13 H4 Z" fill="var(--brand-blue)"/></svg>
      </div>
      <div class="line">info@stillharbor.com
        <svg viewBox="0 0 16 14"><rect x="1" y="2" width="14" height="10" fill="var(--brand-blue)"/><path d="M1 2 L8 8 L15 2" stroke="#fff" stroke-width="1.2" fill="none"/></svg>
      </div>
      <div class="web">www.stillharbor.com</div>
    </div>

    <div class="person">
      <div class="person-name">MARCUS ELDEN</div>
      <div class="person-role">Managing Director</div>
    </div>
  </section>
</main>
</body>
</html>
```